Purchasing community for life science startups needs landing page for collecting of contact adresses

We are the "Vessel Alliance", the first purchasing community for life science startups. The idea is to bundle the needs of several smaller companies (laboratories) and to buy lab consumables and chemicals in larger quantities. This bargaining position, at the end of all participants can buy their products very low prices. In the attached powerpoint file you will find an idea and some elements, which demonstrate a little the style, which came into my mind.
Target Market(s)
Our target customers are startups and smaller biotech companies, which are too small to get the best prices. The aim of this landing page is to collect all interested parties.
Look and feel
Each slider illustrates characteristics of the customer's brand and the style your logo design should communicate.

```html
<!DOCTYPE html>
<html lang="de">
<head>
<meta charset="utf-8">
<title>Vessel Alliance – Gemeinsam einkaufen</title>
<link href="https://fonts.googleapis.com/css2?family=Open+Sans:wght@300;400;600;700&display=swap" rel="stylesheet">
<style>
  :root{
    --blue:#2b86d9;
    --blue-light:#6fb6ee;
    --navy:#1b4e86;
    --text:#4a4f57;
    --muted:#8a9099;
    --band:#8d9298;
    --band-dark:#7b8087;
    --line:#d9dde2;
    --field:#e9ecef;
    --white:#ffffff;
    --footer:#9a9fa5;
    --box:#b98a52;
  }
  *{box-sizing:border-box;margin:0;padding:0}
  html,body{width:880px;height:1200px;overflow:hidden;background:var(--white)}
  body{font-family:"Open Sans",Arial,sans-serif;color:var(--text);position:relative}

  .site-header{height:82px;display:flex;align-items:center;justify-content:center;gap:12px}
  .brand-mark{width:40px;height:40px;background:var(--blue)}
  .brand-name{font-weight:700;font-size:24px;color:var(--navy);letter-spacing:1px;line-height:1.05}
  .brand-name small{display:block;font-size:12px;font-weight:700;letter-spacing:.3px}

  .hero{height:212px;background:linear-gradient(90deg,#dbeefc 0%,var(--blue-light) 35%,var(--blue) 100%);
        display:flex;flex-direction:column;align-items:center;justify-content:center;color:var(--white);text-align:center}
  .hero h1{font-size:40px;font-weight:700;letter-spacing:1px;color:var(--navy)}
  .hero p{font-size:26px;font-weight:300;color:var(--white);margin-top:2px}

  .features{height:143px;display:flex;justify-content:center;gap:120px;padding-top:28px;text-align:center}
  .feature{width:150px}
  .feature svg{display:block;margin:0 auto 10px}
  .feature h3{font-size:11px;font-weight:700;color:var(--navy)}
  .feature p{font-size:10px;color:var(--muted);line-height:1.35}

  .savings-band{height:95px;background:linear-gradient(90deg,var(--band-dark),var(--band));position:relative;overflow:hidden;
        display:flex;align-items:center;justify-content:center;text-align:center;color:var(--white);font-size:19px;font-weight:300;line-height:1.35}
  .savings-band strong{font-weight:700}
  .savings-band .big-figure{position:absolute;right:20px;top:-14px;font-size:120px;font-weight:700;color:rgba(255,255,255,.12)}

  .signup{position:relative;height:445px}
  .box-visual{position:absolute;left:57px;top:33px;width:175px;height:127px;border-radius:4px;
        background:linear-gradient(160deg,#d4a46a,var(--box))}
  .signup-copy{position:absolute;left:300px;width:360px;top:18px;text-align:center}
  .signup-copy h2{font-size:17px;font-weight:700;color:var(--navy);letter-spacing:.5px}
  .benefits{list-style:none;font-size:11px;color:var(--muted);line-height:1.5;margin:4px 0 10px}
  .signup-copy h2.question{font-size:17px}
  .intro{font-size:10.5px;color:var(--muted);line-height:1.45;margin:4px 0 8px}
  .prompt{font-size:12px;font-weight:700;color:var(--text);line-height:1.55}

  .contact-form{position:absolute;left:327px;top:228px;width:300px;padding:12px;border:1px solid var(--line);background:#f6f7f8}
  .field{height:24px;background:var(--white);border:1px solid var(--line);margin-bottom:8px;font-size:10px;color:var(--muted);padding:5px 8px}
  .submit{height:24px;background:var(--blue);color:var(--white);font-size:10px;font-weight:600;text-align:center;line-height:24px;width:60%;margin:8px auto 0}
  .mail-icons{position:absolute;left:650px;top:240px}

  .info-rows{position:absolute;left:0;top:977px;width:880px}
  .info-row{display:flex;gap:26px;align-items:flex-start;padding:0 96px 0 92px;height:66px}
  .info-row svg{flex:none}
  .info-row p{font-size:10.5px;color:var(--muted);line-height:1.45}
  .info-row p strong{color:var(--text);font-weight:700}

  .site-footer{position:absolute;left:0;bottom:0;width:880px;height:22px;background:var(--footer);
        color:var(--white);font-size:9px;line-height:22px;padding-left:92px}
</style>
</head>
<body>

<header class="site-header">
  <div class="brand-mark"></div>
  <div class="brand-name">VESSEL ALLIANCE<small>Einkaufsgemeinschaft Lifescience</small></div>
</header>

<section class="hero">
  <h1>GEMEINSAM EINKAUFEN</h1>
  <p>zu Großhandelspreisen</p>
</section>

<section class="features">
  <div class="feature">
    <svg width="34" height="28" viewBox="0 0 34 28"><rect x="2" y="8" width="30" height="18" fill="none" stroke="#1b4e86" stroke-width="2"/><path d="M10 8V3h14v5" fill="none" stroke="#1b4e86" stroke-width="2"/></svg>
    <h3>Bündeln der Nachfrage</h3>
    <p>viele kleine Labore kaufen gemeinsam</p>
  </div>
  <div class="feature">
    <svg width="34" height="28" viewBox="0 0 34 28"><circle cx="17" cy="14" r="11" fill="none" stroke="#1b4e86" stroke-width="2"/><path d="M12 14l4 4 7-8" fill="none" stroke="#1b4e86" stroke-width="2"/></svg>
    <h3>Günstige Einkaufspreise</h3>
    <p>Verbrauchsmaterial und Chemikalien zu besten Konditionen</p>
  </div>
  <div class="feature">
    <svg width="34" height="28" viewBox="0 0 34 28"><path d="M4 24h26M8 24V12M17 24V6M26 24V15" stroke="#1b4e86" stroke-width="3"/></svg>
    <h3>Stärkere Position</h3>
    <p>Mehr Verhandlungsmacht für junge Unternehmen</p>
  </div>
</section>

<section class="savings-band">
  <span class="big-figure">40%</span>
  <p>Dabei sein bei der ersten Vessel Alliance 2017<br>und <strong>spare bis zu 40% im Einkauf</strong></p>
</section>

<section class="signup">
  <div class="box-visual" role="img" aria-label="Illustration eines Versandkartons mit Laborbedarf"></div>
  <div class="signup-copy">
    <h2>VORTEILE</h2>
    <ul class="benefits">
      <li>Einkauf zu Großhandelspreisen</li>
      <li>Keine Verpflichtung zur Abnahme</li>
      <li>Einfache Abwicklung online</li>
    </ul>
    <h2 class="question">HAST DU INTERESSE AN EINER TEILNAHME?</h2>
    <p class="intro">Dann trag dich jetzt unverbindlich ein. Wir melden uns mit allen Details zur nächsten Einkaufsrunde und den passenden Angeboten.</p>
    <p class="prompt">Welche Artikel interessieren dich?<br>In welchen Mengen benötigst du diese?<br>Welche fehlen noch?</p>
  </div>

  <form class="contact-form">
    <div class="field">Unternehmen</div>
    <div class="field">Vorname</div>
    <div class="field">Nachname</div>
    <div class="field">E-Mail-Adresse</div>
    <div class="submit">Jetzt unverbindlich eintragen</div>
  </form>

  <svg class="mail-icons" width="60" height="60" viewBox="0 0 60 60" aria-hidden="true">
    <g fill="none" stroke="#c3c8ce" stroke-width="1.5">
      <rect x="2" y="4" width="30" height="20"/><path d="M2 4l15 11 15-11"/>
      <rect x="22" y="34" width="34" height="22"/><path d="M22 34l17 12 17-12"/>
    </g>
  </svg>
</section>

<section class="info-rows">
  <div class="info-row">
    <svg width="30" height="30" viewBox="0 0 30 30"><circle cx="10" cy="10" r="5" fill="none" stroke="#4a4f57" stroke-width="1.5"/><circle cx="21" cy="10" r="5" fill="none" stroke="#4a4f57" stroke-width="1.5"/><path d="M2 27c1-7 15-7 16 0M13 27c1-7 15-7 16 0" fill="none" stroke="#4a4f57" stroke-width="1.5"/></svg>
    <p><strong>UNSER ZIEL</strong> ist es, die Nachfrage vieler Startups und kleiner Labore zu bündeln und gemeinsam bessere Preise bei Lieferanten für Laborbedarf zu erzielen.</p>
  </div>
  <div class="info-row">
    <svg width="30" height="30" viewBox="0 0 30 30"><rect x="3" y="8" width="24" height="16" fill="none" stroke="#4a4f57" stroke-width="1.5"/><path d="M3 13h24" stroke="#4a4f57" stroke-width="1.5"/></svg>
    <p><strong>DAS HAUPTVERSPRECHEN:</strong> Wir senden deine Anfrage gesammelt an ausgewählte Händler und verhandeln die Konditionen. Du entscheidest danach frei, ob du bestellst, und profitierst von deutlich reduzierten Preisen.</p>
  </div>
  <div class="info-row">
    <svg width="30" height="30" viewBox="0 0 30 30"><rect x="4" y="4" width="22" height="22" fill="none" stroke="#4a4f57" stroke-width="1.5"/><path d="M9 15l4 4 8-9" fill="none" stroke="#4a4f57" stroke-width="1.5"/></svg>
    <p><strong>SEHR IT SIMPLE.</strong> Eintragen, Bedarf angeben, Angebot erhalten. Wir halten dich per E-Mail auf dem Laufenden und informieren dich rechtzeitig vor dem Start der nächsten Runde der Vessel Alliance.</p>
  </div>
</section>

<footer class="site-footer">© 2017 Vessel Alliance · Impressum · Datenschutz</footer>

</body>
</html>
```